Financial Service Company Need Business Card Design

This is a new startup company, first of its kind to offer this service. We facilitate the movement of deposit funds electronically between home buyers and real estate brokerages.Our customers are DOMIVANS®, real estate brokerages, and home buyers, we identify ourselves as a financial/technology company.
Not looking for anything too flashy. Just a clean design that shows the logo, contact info, etc. Company colors can be seen on attached logo, and 'coming soon page'
www.quorvanta.ca

```html
<!DOCTYPE html>
<html lang="en">
<head>
<meta charset="utf-8">
<title>Quorvanta Business Card</title>
<link rel="stylesheet" href="https://fonts.googleapis.com/css2?family=Saira+Semi+Condensed:wght@400;500;600;700&display=swap">
<style>
  :root {
    --page-bg: #f2f2f2;
    --brand-grey: #807e80;
    --band-grey: #6d6c6f;
    --brand-orange: #e8522a;
    --band-orange: #ee6238;
    --ink-light: #ffffff;
    --card-shadow: rgba(0, 0, 0, 0.18);
  }
  * { box-sizing: border-box; margin: 0; padding: 0; }
  html, body {
    width: 1200px;
    height: 1000px;
    overflow: hidden;
    background: var(--page-bg);
    font-family: "Saira Semi Condensed", "Arial Narrow", sans-serif;
  }
  .sheet {
    width: 1200px;
    height: 1000px;
    display: flex;
    flex-direction: column;
    align-items: center;
    justify-content: center;
    gap: 60px;
  }
  .card {
    position: relative;
    width: 740px;
    height: 423px;
    overflow: hidden;
    box-shadow: 0 6px 18px var(--card-shadow);
  }
  /* Front */
  .card--front {
    background: var(--brand-grey);
    display: flex;
    align-items: center;
    justify-content: center;
  }
  .card--front .band {
    position: absolute;
    left: 0;
    width: 100%;
    height: 32px;
    background: var(--band-orange);
  }
  .card--front .band--top { top: 0; }
  .card--front .band--bottom { bottom: 0; }
  .brand {
    display: flex;
    align-items: center;
    gap: 18px;
    color: var(--ink-light);
    font-weight: 600;
    letter-spacing: 0.5px;
  }
  .brand-square {
    background: var(--ink-light);
    flex: none;
  }
  .card--front .brand { font-size: 78px; }
  .card--front .brand-square { width: 52px; height: 52px; }

  /* Back */
  .card--back {
    background: var(--brand-orange);
    color: var(--ink-light);
    padding: 44px 52px 0;
  }
  .card--back .band--bottom {
    position: absolute;
    left: 0;
    bottom: 0;
    width: 100%;
    height: 30px;
    background: var(--band-grey);
  }
  .card--back .brand { font-size: 40px; gap: 12px; }
  .card--back .brand-square { width: 26px; height: 26px; }
  .person { margin-top: 10px; }
  .person-name { font-size: 30px; font-weight: 700; line-height: 1.1; }
  .person-title { font-size: 17px; font-weight: 500; line-height: 1.3; }
  .contact { margin-top: 16px; font-size: 21px; font-weight: 600; line-height: 1.45; }
  .contact .label { margin-right: 8px; }
  .contact .gap { margin-left: 22px; }
  .website {
    position: absolute;
    left: 52px;
    bottom: 46px;
    font-size: 24px;
    font-weight: 500;
    letter-spacing: 2px;
    text-transform: uppercase;
    color: var(--band-grey);
  }
</style>
</head>
<body>
<main class="sheet">
  <section class="card card--front" aria-label="Card front">
    <div class="band band--top"></div>
    <div class="brand">
      <span class="brand-square"></span>
      <span class="brand-name">Quorvanta</span>
    </div>
    <div class="band band--bottom"></div>
  </section>

  <section class="card card--back" aria-label="Card back">
    <div class="brand">
      <span class="brand-square"></span>
      <span class="brand-name">Quorvanta</span>
    </div>
    <div class="person">
      <p class="person-name">Daniel Reyes</p>
      <p class="person-title">Change</p>
    </div>
    <div class="contact">
      <p>dreyes@quorvanta.ca</p>
      <p><span class="label">Phone</span>123 456 789<span class="gap label">Mobile</span>123 456 789</p>
      <p>123 Main Avenue<span class="gap">Anytown</span></p>
    </div>
    <p class="website">www.quorvanta.ca</p>
    <div class="band--bottom"></div>
  </section>
</main>
</body>
</html>
```